Business Card Design Project

We need a redesign of our business card.
We are a Consulting Property Developer called The Kestrel Group
Updates

Thank you all for submissions. Just waiting on managment to decide.

Thank you,

Dorinda

Industry/Entity Type

Business

Requirements
Must have
• we like having the KG a focus in the back ground or on the side
Kestrel is our company colour

the wording - property development
and - premium accommodation

our website www.kestrelgroup-example.com.au

persons name
title

p: 1300 482917 f: 1300 482915 m: 0417593824
PO Box 5817, Brindlevale Qld 4178
e: admin@kestrelgroup-example.com.au

```html
<!DOCTYPE html>
<html lang="en">
<head>
<meta charset="utf-8">
<title>The Kestrel Group – Business Card</title>
<link rel="stylesheet" href="https://fonts.googleapis.com/css2?family=Cinzel:wght@400;500&family=Source+Sans+3:wght@400;600&display=swap">
<style>
  :root {
    --kestrel: #9b1b30;
    --kestrel-soft: #d9a9ae;
    --silver: #c9c9cb;
    --grey-text: #8e8e90;
    --ink: #2b2b2b;
    --card-white: #ffffff;
    --backdrop: #5c3621;
  }
  * { box-sizing: border-box; margin: 0; padding: 0; }
  html, body { width: 1200px; height: 447px; overflow: hidden; }
  body {
    position: relative;
    background: var(--backdrop);
    font-family: "Source Sans 3", Arial, sans-serif;
  }
  .card {
    position: absolute;
    top: 75px;
    width: 543px;
    height: 310px;
    border-radius: 22px;
    box-shadow: 0 4px 14px rgba(0,0,0,0.35);
  }
  .card-front { left: 40px; background: var(--card-white); }
  .card-back { left: 612px; background: var(--kestrel); }

  /* Front */
  .brand-name {
    position: absolute;
    left: 58px; top: 38px;
    font-size: 40px;
    font-weight: 400;
    color: var(--kestrel);
    letter-spacing: -0.5px;
  }
  .brand-rule {
    position: absolute;
    left: 56px; top: 82px;
    width: 400px; height: 1px;
    background: var(--grey-text);
  }
  .contact-list {
    position: absolute;
    left: 32px; top: 170px;
    list-style: none;
    font-size: 13.5px;
    color: var(--ink);
    line-height: 17px;
  }
  .contact-list li { display: flex; align-items: center; gap: 6px; }
  .contact-list svg { width: 11px; height: 11px; fill: var(--kestrel); flex: none; }
  .contact-web {
    position: absolute;
    left: 33px; top: 243px;
    font-size: 13px;
    letter-spacing: 1px;
    color: var(--kestrel);
  }
  .contact-address {
    position: absolute;
    left: 33px; top: 270px;
    font-size: 13.5px;
    color: var(--ink);
  }
  .person {
    position: absolute;
    left: 300px; top: 170px;
    width: 220px;
    text-align: center;
  }
  .person-name {
    font-family: "Cinzel", Georgia, serif;
    font-size: 23px;
    color: var(--kestrel);
    line-height: 26px;
  }
  .person-title {
    font-size: 13px;
    letter-spacing: 0.5px;
    color: var(--ink);
    margin-top: 6px;
  }
  .person-mark {
    display: block;
    margin: 10px auto 0;
    width: 58px; height: 58px;
    border-radius: 50%;
    border: 2px solid var(--kestrel-soft);
  }

  /* Back */
  .back-mark {
    position: absolute;
    left: 0; right: 0; top: 95px;
    display: flex; align-items: center; justify-content: center; gap: 14px;
  }
  .back-mark-circle {
    width: 46px; height: 46px;
    border-radius: 50%;
    border: 2px solid var(--silver);
  }
  .back-mark-name {
    font-size: 34px;
    font-weight: 400;
    color: var(--silver);
  }
  .tagline {
    position: absolute;
    left: 0; right: 0; top: 237px;
    text-align: center;
    font-size: 15.5px;
    letter-spacing: 0.8px;
    color: #f3e6e8;
  }
  .tagline .amp {
    font-family: "Cinzel", Georgia, serif;
    font-size: 22px;
    margin: 0 6px;
  }
  .back-web {
    position: absolute;
    left: 0; right: 0; top: 272px;
    text-align: center;
    font-size: 14px;
    letter-spacing: 1.5px;
    color: var(--silver);
  }
</style>
</head>
<body>
  <section class="card card-front">
    <div class="brand-name">The Kestrel Group</div>
    <div class="brand-rule"></div>

    <ul class="contact-list">
      <li><svg viewBox="0 0 12 12"><path d="M3 0.5l2 2.5-1.2 1.3c.6 1.4 1.6 2.4 3 3L8 6l2.5 2-1 2.5C5 10.5 1.5 7 1.5 2.5z"/></svg>1300 482917</li>
      <li><svg viewBox="0 0 12 12"><rect x="3" y="1" width="6" height="3"/><rect x="1" y="4.5" width="10" height="5" rx="1"/><rect x="3" y="8" width="6" height="3"/></svg>1300 482915</li>
      <li><svg viewBox="0 0 12 12"><rect x="3" y="0.5" width="6" height="11" rx="1"/></svg>0417593824</li>
      <li><svg viewBox="0 0 12 12"><path d="M0.5 2.5h11v7h-11z M0.5 2.5l5.5 4 5.5-4" fill="none" stroke="#9b1b30" stroke-width="1.2"/></svg>admin@kestrelgroup-example.com.au</li>
    </ul>
    <div class="contact-web">WWW.KESTRELGROUP-EXAMPLE.COM.AU</div>
    <div class="contact-address">PO Box 5817, Brindlevale Qld 4178</div>

    <div class="person">
      <div class="person-name">PERSON NAME</div>
      <div class="person-title">DIRECTOR</div>
      <span class="person-mark" aria-hidden="true"></span>
    </div>
  </section>

  <section class="card card-back">
    <div class="back-mark">
      <span class="back-mark-circle" aria-hidden="true"></span>
      <span class="back-mark-name">The Kestrel Group</span>
    </div>
    <div class="tagline">PROPERTY DEVELOPMENT<span class="amp">&amp;</span>PREMIUM ACCOMMODATION</div>
    <div class="back-web">www.KESTRELGROUP-EXAMPLE.com.au</div>
  </section>
</body>
</html>
```